Electrical construction company
Industrial Construction, mining construction, Electrical works
Creative Brief
Construction
brightlinepowerworks.com.au
Electrical construction. Experienced in the construction industry,20 year. High quality work First class customer services Able to be flexible and suit customer requirements Provide QA documention and qualified testers. Hazardous Area trained personel 5 star safety rating
Modern
Blue same as in logo
PixelRidge PixelRidge
PH, Kindly check your private messages. Thanks!
owenharlow owenharlow
#59 can you use the picture i suppied as the back drop, the one of the plant. Thankyou
Phone numnber is 1800 VOLTEK Address is 17/9 Marlin Court, Belmont, western australia Thankyou
#50 can you use the picture provided of the plant Thankyou
Will need to include Lic. No. EC38157 somewhere also
Not so interested about have a testimonial on he front page Maybe use the other pictures as the main thankyou
i have payed 700 would have thought the prise was 700?
Would like the page to fit on the page without scrolling down
Like the idea of the map with address
HubKeeper HubKeeper

```html
<!DOCTYPE html>
<html lang="en">
<head>
<meta charset="utf-8">
<title>Brightline Powerworks – Electrical Construction</title>
<link href="https://fonts.googleapis.com/css2?family=Oswald:wght@400;500;700&family=Roboto+Condensed:wght@400;700&display=swap" rel="stylesheet">
<style>
  :root{
    --brand-blue:#1f5fb0;
    --nav-blue:#2a6cc0;
    --nav-red:#d7191f;
    --accent-green:#3d9a2b;
    --button-green:#8cbf1a;
    --text-grey:#555a60;
    --heading-dark:#2b2f33;
    --band-grey:#d9dadb;
    --panel-light:#f1f1f1;
    --footer-dark:#2b2b2b;
    --footer-text:#a8b33a;
  }
  *{margin:0;padding:0;box-sizing:border-box}
  html,body{width:1200px;height:955px;overflow:hidden;background:#fff}
  body{position:relative;font-family:"Roboto Condensed",sans-serif;color:var(--text-grey)}

  .site-header{position:absolute;left:0;top:0;width:1200px;height:85px;background:#fff}
  .brand{position:absolute;left:98px;top:14px;display:flex;align-items:center;gap:12px}
  .brand-mark{width:52px;height:52px;border-radius:50%;background:var(--brand-blue)}
  .brand-name{font-family:"Oswald",sans-serif;font-weight:700;font-size:30px;color:var(--brand-blue);letter-spacing:1px;text-transform:uppercase}

  .contact-bar{position:absolute;left:590px;top:8px;display:flex;align-items:center;gap:8px;font-size:14px;color:var(--heading-dark)}
  .contact-bar .phone{font-family:"Oswald",sans-serif;font-size:24px;color:var(--brand-blue);margin-right:16px}
  .contact-bar .email{color:var(--nav-red)}
  .contact-icon{width:22px;height:22px}

  .main-nav{position:absolute;left:547px;top:46px;width:558px;height:39px;background:var(--nav-blue);display:flex;border-radius:3px 3px 0 0}
  .main-nav a{flex:1;display:flex;align-items:center;justify-content:center;color:#fff;font-family:"Oswald",sans-serif;font-size:15px;text-decoration:none;border-right:1px solid rgba(255,255,255,.2)}
  .main-nav a.active{background:var(--nav-red)}

  .hero{position:absolute;left:0;top:85px;width:1200px;height:354px;background:linear-gradient(180deg,#1b3a63 0%,#2b5a88 45%,#34688f 62%,#c48a3e 80%,#2c3b4c 100%)}
  .hero-line{position:absolute;left:160px;font-family:"Oswald",sans-serif;font-weight:500;color:#fff;text-transform:uppercase;display:flex;align-items:center;padding:0 14px;letter-spacing:1px}
  .hero-line.green{top:194px;height:64px;width:441px;background:var(--accent-green);font-size:40px}
  .hero-line.red{top:271px;height:64px;width:632px;background:var(--nav-red);font-size:40px}
  .slider-arrow{position:absolute;top:248px;width:38px;height:38px}
  .slider-arrow.prev{left:94px}
  .slider-arrow.next{left:1067px}

  .services-band{position:absolute;left:0;top:444px;width:1200px;height:80px;background:var(--band-grey)}
  .services-panel{position:absolute;left:103px;top:444px;width:1001px;height:80px}
  .service{position:absolute;top:457px;display:flex;align-items:center;gap:10px}
  .service-icon{width:54px;height:54px}
  .service-title{font-family:"Oswald",sans-serif;font-weight:500;font-size:32px;line-height:1;color:var(--heading-dark)}
  .service-sub{font-family:"Oswald",sans-serif;font-size:13px;color:var(--text-grey);text-transform:uppercase;margin-top:2px}
  .service.industrial{left:152px}
  .service.mining{left:513px}
  .service.electrical{left:815px}

  .photo{position:absolute;top:555px;height:278px}
  .photo.plans{left:124px;width:173px;background:linear-gradient(160deg,#e9f0f7,#9fb8d3)}
  .photo.engineer{left:315px;width:173px;background:linear-gradient(170deg,#d9e4ee,#4f6d8f)}
  .photo.supervisor{left:503px;width:176px;background:linear-gradient(170deg,#eef1f3,#b3b9be)}

  .welcome{position:absolute;left:704px;top:553px;width:384px}
  .welcome h1{font-family:"Roboto Condensed",sans-serif;font-weight:400;font-size:22px;color:var(--heading-dark)}
  .welcome h1 span{font-family:"Oswald",sans-serif;font-weight:700;color:var(--brand-blue)}
  .welcome p{margin-top:6px;font-size:16.5px;line-height:1.45;color:var(--text-grey)}
  .read-more{position:absolute;left:704px;top:735px;width:116px;height:34px;background:var(--button-green);color:#fff;font-family:"Oswald",sans-serif;font-size:15px;display:flex;align-items:center;justify-content:center;text-decoration:none}

  .site-footer{position:absolute;left:0;top:890px;width:1200px;height:65px;background:var(--footer-dark)}
  .footer-note{position:absolute;left:90px;top:22px;font-size:14px;color:var(--footer-text)}
  .social{position:absolute;left:975px;top:17px;display:flex;gap:10px}
  .social span{width:30px;height:30px;border-radius:50%;background:var(--button-green)}
</style>
</head>
<body>

<header class="site-header">
  <div class="brand">
    <span class="brand-mark"></span>
    <span class="brand-name">Brightline Powerworks</span>
  </div>
  <div class="contact-bar">
    <svg class="contact-icon" viewBox="0 0 22 22"><rect x="2" y="2" width="18" height="18" rx="3" fill="#8a9099"/><path d="M7 6c1 0 2 2 2 3s-1 1-1 2 2 3 3 3 1-1 2-1 3 1 3 2-1 2-2 2c-4 0-9-5-9-9 0-1 1-2 2-2z" fill="#fff"/></svg>
    <span>contact us:</span>
    <span class="phone">900-555-0142</span>
    <svg class="contact-icon" viewBox="0 0 22 22"><circle cx="11" cy="11" r="10" fill="#8a9099"/><rect x="5" y="7" width="12" height="8" fill="#fff"/><path d="M5 7l6 5 6-5" stroke="#8a9099" fill="none"/></svg>
    <span>email :</span>
    <span class="email">info@brightlinepowerworks.com.au</span>
  </div>
  <nav class="main-nav">
    <a class="active" href="#">HOME</a>
    <a href="#">ABOUT US</a>
    <a href="#">SERVICES</a>
    <a href="#">NEWS</a>
    <a href="#">CLIENTS</a>
    <a href="#">CONTACT</a>
  </nav>
</header>

<section class="hero" role="img" aria-label="Industrial processing plant lit up at dusk">
</section>
<div class="hero-line green" style="top:279px">High Quality Work</div>
<div class="hero-line red" style="top:356px">First Class Customer Services</div>
<svg class="slider-arrow prev" style="top:333px" viewBox="0 0 38 38"><circle cx="19" cy="19" r="18" fill="#1c1c1c"/><path d="M22 11l-8 8 8 8" stroke="#fff" stroke-width="3" fill="none"/></svg>
<svg class="slider-arrow next" style="top:333px" viewBox="0 0 38 38"><circle cx="19" cy="19" r="18" fill="#1c1c1c"/><path d="M16 11l8 8-8 8" stroke="#fff" stroke-width="3" fill="none"/></svg>

<div class="services-band"></div>
<svg class="services-panel" viewBox="0 0 1001 80" preserveAspectRatio="none">
  <defs><linearGradient id="panelShade" x1="0" y1="0" x2="0" y2="1"><stop offset="0" stop-color="#fafafa"/><stop offset="1" stop-color="#e4e4e4"/></linearGradient></defs>
  <path d="M22 0H979L955 80H46Z" fill="url(#panelShade)"/>
</svg>

<div class="service industrial">
  <svg class="service-icon" viewBox="0 0 54 54"><circle cx="27" cy="27" r="26" fill="#fff" stroke="#cfcfcf"/><path d="M13 38V24l7 4v-4l7 4v-4l7 4V16h6v22Z" fill="#333"/></svg>
  <div><div class="service-title">INDUSTRIAL</div><div class="service-sub">Construction</div></div>
</div>
<div class="service mining">
  <svg class="service-icon" viewBox="0 0 54 54"><circle cx="27" cy="27" r="26" fill="#fff" stroke="#cfcfcf"/><path d="M15 19q12-8 24 0" stroke="#333" stroke-width="4" fill="none"/><path d="M27 16l-8 24" stroke="#333" stroke-width="4"/></svg>
  <div><div class="service-title">MINING</div><div class="service-sub">Construction</div></div>
</div>
<div class="service electrical">
  <svg class="service-icon" viewBox="0 0 54 54"><circle cx="27" cy="27" r="26" fill="#fff" stroke="#cfcfcf"/><circle cx="27" cy="23" r="9" fill="#333"/><rect x="23" y="31" width="8" height="8" fill="#333"/></svg>
  <div><div class="service-title">ELECTRICAL</div><div class="service-sub">Works</div></div>
</div>

<div class="photo plans" role="img" aria-label="Rolled engineering blueprints and drafting tools"></div>
<div class="photo engineer" role="img" aria-label="Smiling engineer holding a blue hard hat"></div>
<div class="photo supervisor" role="img" aria-label="Senior site supervisor in a yellow hard hat reviewing plans"></div>

<section class="welcome">
  <h1><span>WELCOME</span> Electrical construction company</h1>
  <p>Electrical construction. Experienced in the construction industry,20 year. High quality work First class customer services Able to be flexible and suit customer requirements Provide QA documention and qualified testers. Hazardous Area trained personel 5 star safety rating.</p>
</section>
<a class="read-more" href="#">READ MORE</a>

<footer class="site-footer">
  <div class="footer-note">brightlinepowerworks.com.au © 2012 | Privacy Policy</div>
  <div class="social"><span></span><span></span><span></span><span></span></div>
</footer>

</body>
</html>
```